Landing page for buying gold and stamps

Create a landing page for our purchase. We buy postage stamps, franked goods, gold coins, scrap gold, silver money, etc. We don't want to sell anything to people, we just shop. So the visitors should send their old gold, their stamps, etc. by post. We then estimate the value and transfer the money by bank or you can collect it in cash.

The visitor should see what he can sell. If he fills in his contact details, he will receive our purchase form and the mailing label by post so that he can send in his sales goods free of charge. Or he can call us or write an e-mail and come to us directly.

We buy:
When the form is filled out, an email will be sent to our address with the following data:
Surname
First name
Street, Nr.
Post loan number
place
What do you want to sell

In the appendix I have added designs of flyers. You can see what we buy on it. What is missing on the flyer, however, are stamps, franking goods and rarities. In addition, the design should be similar. The logo can also be used.

In addition, the following text should be on the page:
Do you need help selling an inherited collection? Feel free to contact us. We are happy to help. We have been in the stamp and coin trade for nearly 100 years.

I have also attached a picture of the stamp as an attachment. This should also be put on the side with old gold and gold coins.

And here you will find our current purchase pages:
https://www.briefhaus-tanner.ch/ankauf-gold-und-silber
https://www.briefhaus-tanner.ch/ankauf-frankatur

Competitors' pages:
https://www.wertsachenpost.ch/goldankauf/
https://www.praegehof-lindt.ch/ankauf-1/altgold-ankauf1.html

Target Market(s)

Private persons

Font styles to use
Serif
Sans Serif

Requirements
Must have
• It must be clear that anyone who wants to sell their gold, stamps or coins can do so easily from home by post. You no longer have to go to a store.
Steps to Sell:
1. You fill out your contact details
2. We will send you a form and a label for shipping (no postage for you!)
3. You will receive a non-binding purchase offer
4. You will receive the money transferred or you can collect it in cash (or we will send you the valuables you have sent back)

You have no costs! Simply sell your gold or stamps from home.

```html
<!DOCTYPE html>
<html lang="en">
<head>
<meta charset="utf-8">
<title>Briefhaus Tanner – Sell gold and stamps from home</title>
<link rel="stylesheet" href="https://fonts.googleapis.com/css2?family=Lora:ital,wght@0,400;1,400;1,700&family=Raleway:wght@400;500;600;700&family=Lato:wght@400;700&display=swap">
<style>
:root{
  --blue:#2f3395;
  --red:#e74c3c;
  --dark:#333333;
  --darker:#2a2a2a;
  --ink:#2b2b2b;
  --muted:#666666;
  --line:#e6e6e6;
  --white:#ffffff;
}
*{margin:0;padding:0;box-sizing:border-box}
html,body{width:1200px;height:2936px;overflow:hidden;background:var(--white)}
.page{position:relative;width:1200px;height:2936px;font-family:"Lato",sans-serif;color:var(--ink)}
.abs{position:absolute}
.serif-i{font-family:"Lora",serif;font-style:italic}

/* top bar */
.topbar{left:0;top:0;width:1200px;height:34px;border-bottom:1px solid var(--line);border-top:1px solid var(--line)}
.topbar a{position:absolute;top:10px;font-size:10px;color:#444;text-decoration:none;font-family:"Raleway",sans-serif}
/* header */
.header{left:0;top:34px;width:1200px;height:82px;border-bottom:1px solid var(--line)}
.brand{position:absolute;left:172px;top:24px;display:flex;align-items:center;gap:8px;font-family:"Raleway",sans-serif;font-weight:700;font-size:21px;color:var(--red);letter-spacing:.5px}
.brand i{display:block;width:14px;height:14px;background:var(--blue)}
.nav a{position:absolute;top:38px;font-family:"Raleway",sans-serif;font-weight:600;font-size:11.5px;letter-spacing:1px;color:#333;text-decoration:none}
/* hero */
.hero{left:0;top:116px;width:1200px;height:485px;background:radial-gradient(ellipse at 35% 65%,#a48f6e 0%,#857a93 35%,#726fa3 65%,#5e5a8e 100%)}
.hero h1{position:absolute;left:0;width:1200px;top:70px;text-align:center;font-weight:400;font-size:38px;line-height:48px;color:var(--white)}
.helpband{left:0;top:601px;width:1200px;height:115px;background:var(--blue)}
.helpband p{position:absolute;left:171px;top:30px;font-family:"Raleway",sans-serif;font-size:20.5px;line-height:25px;letter-spacing:.6px;color:var(--white)}
.helpband svg{position:absolute;left:688px;top:34px}
/* form */
.sellform{left:772px;top:329px;width:256px;height:388px;background:var(--dark);padding-top:10px}
.sellform h2{text-align:center;font-family:"Raleway",sans-serif;font-weight:600;font-size:21px;color:var(--white);height:47px;line-height:26px}
.sellform .field{display:block;margin:0 0 13px 23px;width:212px;height:32px;border:0;background:var(--white);padding:0 11px;font-family:"Raleway",sans-serif;font-size:13px;color:#999;line-height:32px;letter-spacing:.5px}
.sellform .send{display:block;margin:5px 0 0 23px;width:212px;height:30px;background:var(--red);color:var(--white);text-align:center;line-height:30px;font-family:"Raleway",sans-serif;font-weight:700;font-size:12px;letter-spacing:.5px}
/* section titles */
.sectitle{left:0;width:1200px;text-align:center;font-weight:700;font-size:25px;color:var(--ink)}
.secsub{left:0;width:1200px;text-align:center;font-size:18px;color:#444}
/* goods */
.good{width:270px}
.good svg{display:block}
.good h3{position:absolute;left:0;font-family:"Raleway",sans-serif;font-weight:600;font-size:13.5px;letter-spacing:1px;color:#222;white-space:nowrap}
.good p{position:absolute;left:0;width:270px;font-size:11.5px;line-height:19px;color:var(--muted)}
/* contact columns */
.way{top:1492px;width:400px;height:269px;color:var(--white);padding:46px 0 0 46px}
.way h3{font-family:"Lora",serif;font-style:italic;font-weight:700;font-size:19px;margin-bottom:22px}
.way p{width:290px;font-size:11.5px;line-height:19px}
.way .call{font-family:"Lora",serif;font-style:italic;font-weight:700;font-size:22px;margin-top:20px}
.way .btn{display:inline-block;margin-top:23px;margin-left:-2px;height:35px;line-height:31px;padding:0 14px;border:2px solid var(--white);font-family:"Raleway",sans-serif;font-weight:700;font-size:11px;letter-spacing:.5px}
/* steps */
.step{width:410px}
.step h4{font-family:"Raleway",sans-serif;font-weight:500;font-size:14px;line-height:17px;color:#222}
.step p{margin-top:14px;font-size:11.5px;line-height:19px;color:var(--muted)}
.rule{height:1px;background:var(--line);width:410px}
/* quote */
.quote{left:0;top:2433px;width:1200px;height:253px;background:linear-gradient(135deg,#34389a,#2e3290 60%,#3a3d9c)}
.quote p{position:absolute;left:0;width:1200px;top:88px;text-align:center;font-size:31px;line-height:41px;color:var(--white)}
/* footer */
.footer{left:0;top:2686px;width:1200px;height:179px;background:var(--dark);color:#ccc}
.footer h5{position:absolute;top:44px;font-family:"Raleway",sans-serif;font-weight:600;font-size:12px;letter-spacing:1.2px;color:#eee}
.footer ul{position:absolute;top:80px;list-style:none}
.footer li{font-size:10.5px;height:22.5px;color:#ccc}
.footer li::before{content:"›";margin-right:8px}
.footer .phone{position:absolute;left:813px;top:38px;font-family:"Lora",serif;font-size:18px;color:#eee}
.footer .mail{position:absolute;left:813px;top:72px;font-family:"Raleway",sans-serif;font-weight:700;font-size:10px;letter-spacing:.6px;color:#eee}
.footer .social{position:absolute;left:812px;top:104px;display:flex;align-items:center;gap:8px}
.footer .social i{display:block;width:28px;height:28px;background:#3b5290}
.footer .social span{font-size:8px;line-height:14px;color:#eee}
.legal{left:0;top:2865px;width:1200px;height:71px;background:var(--darker)}
.legal p{position:absolute;left:172px;font-size:9.5px;color:#777}
</style>
</head>
<body>
<div class="page">

  <div class="abs topbar">
    <a style="left:788px">Menu1</a><a style="left:853px">Menu2</a><a style="left:918px">Menu3</a><a style="left:984px">Menu4</a>
  </div>

  <header class="abs header">
    <div class="brand"><i></i>BRIEFHAUS TANNER</div>
    <nav class="nav">
      <a style="left:544px">HOME</a><a style="left:604px">FEATURES</a><a style="left:689px">PAGES</a>
      <a style="left:754px">ADD MEMU</a><a style="left:845px">PAGES</a><a style="left:909px">ADD MENU</a>
      <svg style="position:absolute;left:1008px;top:40px" width="11" height="11" viewBox="0 0 11 11"><circle cx="4.5" cy="4.5" r="3.3" fill="none" stroke="#333" stroke-width="1.6"/><line x1="7" y1="7" x2="10" y2="10" stroke="#333" stroke-width="1.8"/></svg>
    </nav>
  </header>

  <section class="abs hero" role="img" aria-label="Close-up photo of gold jewellery and a pearl with a violet tint">
    <h1 class="serif-i">You have no costs! Simply sell your gold<br>or stamps from home</h1>
  </section>

  <div class="abs helpband">
    <p>Do you need help selling an inherited collection?<br>Feel free to contact us. We are happy to help.</p>
    <svg width="18" height="18" viewBox="0 0 18 18"><circle cx="9" cy="9" r="9" fill="#fff"/><path d="M5 9h7M9 5.5 12.5 9 9 12.5" stroke="#2f3395" stroke-width="2.2" fill="none" stroke-linecap="round" stroke-linejoin="round"/></svg>
  </div>

  <form class="abs sellform">
    <h2>START SELLING</h2>
    <div class="field">Surname</div>
    <div class="field">First name</div>
    <div class="field">Street, Nr.</div>
    <div class="field">Post loan number</div>
    <div class="field">Place</div>
    <div class="field">What do you want to sell</div>
    <div class="send">SEND</div>
  </form>

  <h2 class="abs sectitle serif-i" style="top:824px">What you can sell</h2>
  <p class="abs secsub serif-i" style="top:873px">Lorem ipsum dolor sit amet, consectetur adipiscing elit</p>

  <div class="abs good" style="left:170px;top:942px">
    <svg width="44" height="50" viewBox="0 0 44 50"><rect x="2" y="2" width="40" height="46" fill="none" stroke="#333" stroke-width="4" stroke-dasharray="4 2"/><rect x="8" y="8" width="28" height="34" fill="none" stroke="#333" stroke-width="2"/><circle cx="22" cy="25" r="9" fill="#333"/></svg>
    <h3 style="top:71px">POSTAGE STAMPS</h3>
    <p style="top:98px">Duis sit amet sollicitudin ante, nonpulvinar orci. Interdum et malesuada fames ac ante ipsum primis in faucibus. Duis sit amet sollicitudin ante, nonpulvinar orci. Interdum et malesuada fames ac ante ipsum primis in faucibus.</p>
  </div>
  <div class="abs good" style="left:470px;top:942px">
    <svg width="62" height="48" viewBox="0 0 62 48"><rect x="2" y="3" width="34" height="34" fill="none" stroke="#333" stroke-width="4" stroke-dasharray="4 2"/><path d="M10 28 L18 14 L28 28 Z" fill="#333"/><path d="M24 36 q8 -12 16 0 t20 4" fill="none" stroke="#333" stroke-width="3"/></svg>
    <h3 style="top:71px">FRANKED GOODS</h3>
    <p style="top:98px">Duis sit amet sollicitudin ante, nonpulvinar orci. Interdum et malesuada fames ac ante ipsum primis in faucibus. Duis sit amet sollicitudin ante, nonpulvinar orci. Interdum et malesuada fames ac ante ipsum primis in faucibus.</p>
  </div>
  <div class="abs good" style="left:770px;top:942px">
    <svg width="60" height="50" viewBox="0 0 60 50"><ellipse cx="20" cy="34" rx="18" ry="8" fill="#333"/><ellipse cx="38" cy="30" rx="20" ry="9" fill="#333" stroke="#fff" stroke-width="2"/><ellipse cx="38" cy="27" rx="20" ry="9" fill="#333" stroke="#fff" stroke-width="2"/></svg>
    <h3 style="top:71px">GOLD COINS</h3>
    <p style="top:98px">Duis sit amet sollicitudin ante, nonpulvinar orci. Interdum et malesuada fames ac ante ipsum primis in faucibus. Duis sit amet sollicitudin ante, nonpulvinar orci. Interdum et malesuada fames ac ante ipsum primis in faucibus.</p>
  </div>
  <div class="abs good" style="left:170px;top:1188px">
    <svg width="62" height="50" viewBox="0 0 62 50"><path d="M0 36 L22 26 L34 34 L12 46 Z" fill="#333"/><path d="M16 32 L34 10 L46 16 L30 40 Z" fill="#333" stroke="#fff" stroke-width="2"/><path d="M34 36 L46 6 L56 10 L62 36 L48 46 Z" fill="#333" stroke="#fff" stroke-width="2"/></svg>
    <h3 style="top:72px">SCRAP GOLD</h3>
    <p style="top:109px">Duis sit amet sollicitudin ante, nonpulvinar orci. Interdum et malesuada fames ac ante ipsum primis in faucibus. Duis sit amet sollicitudin ante, nonpulvinar orci. Interdum et malesuada fames ac ante ipsum primis in faucibus.</p>
  </div>
  <div class="abs good" style="left:471px;top:1188px">
    <svg width="64" height="50" viewBox="0 0 64 50"><ellipse cx="18" cy="36" rx="16" ry="9" fill="#333" transform="rotate(-20 18 36)"/><ellipse cx="40" cy="36" rx="22" ry="7" fill="#333" stroke="#fff" stroke-width="2"/><ellipse cx="40" cy="30" rx="20" ry="7" fill="#333" stroke="#fff" stroke-width="2"/></svg>
    <h3 style="top:72px">SILVER MONEY</h3>
    <p style="top:109px">Duis sit amet sollicitudin ante, nonpulvinar orci. Interdum et malesuada fames ac ante ipsum primis in faucibus. Duis sit amet sollicitudin ante, nonpulvinar orci. Interdum et malesuada fames ac ante ipsum primis in faucibus.</p>
  </div>

  <div class="abs way" style="left:0;background:var(--blue)">
    <h3>Call us to sell</h3>
    <p>Lorem ipsum dolor sit amet, consectetur adipisicing ero quod consequuntur quibusdam, enim expedita nesciunt incidunt accusamus necessitatibus modi ad. enim expedita nesciunt</p>
    <div class="call">Call:&nbsp; 9831704400</div>
  </div>
  <div class="abs way" style="left:400px;background:var(--red)">
    <h3>Sell by email</h3>
    <p>Lorem ipsum dolor sit amet, consectetur adipisicing ero quod consequuntur quibusdam, enim expedita nesciunt incidunt accusamus necessitatibus modi ad. enim expedita nesciunt</p>
    <span class="btn">SEND MAIL</span>
  </div>
  <div class="abs way" style="left:800px;background:var(--blue)">
    <h3>Fill out your details</h3>
    <p>Lorem ipsum dolor sit amet, consectetur adipisicing ero quod consequuntur quibusdam, enim expedita nesciunt incidunt accusamus necessitatibus modi ad. enim expedita nesciunt</p>
    <span class="btn">FILL THE FORM</span>
  </div>

  <h2 class="abs sectitle serif-i" style="top:1872px">Steps to sell</h2>
  <p class="abs secsub serif-i" style="top:1921px">Nunc finibus purus id erat ultrices, id ultricies urna interdum.</p>

  <div class="abs step" style="left:172px;top:2006px">
    <h4>1. You fill out your contact details</h4>
    <p>Lorem ipsum dolor sit amet, consectetur adipiscing elit. Donec lobortis nisi vel lectus mattis venenatis. Etiam iaculis volutpat congue. Nam eu faucibus massa. Praesent congue et neque vitae sollicitudin. Pellentesque habitant morbi tristique senectus et netus et malesuada fames vitae,</p>
  </div>
  <div class="abs rule" style="left:172px;top:2155px"></div>
  <div class="abs step" style="left:172px;top:2196px">
    <h4>3. You will receive a non-binding purchase offer</h4>
    <p>Lorem ipsum dolor sit amet, consectetur adipiscing elit. Donec lobortis nisi vel lectus mattis venenatis. Etiam iaculis volutpat congue. Nam eu faucibus massa. Praesent congue et neque vitae sollicitudin. Pellentesque habitant morbi tristique senectus et netus et malesuada fames ac turpis egestas. Donec eget blandit metus. Suspendisse vel orci fermentum, bibendum quam</p>
  </div>
  <div class="abs step" style="left:617px;top:2006px">
    <h4>2. We will send you a form and a label for shipping<br>(no postage for you!)</h4>
    <p>Lorem ipsum dolor sit amet, consectetur adipiscing elit. Donec lobortis nisi vel lectus mattis venenatis. Etiam iaculis volutpat congue. Nam eu faucibus massa. Praesent congue et neque vitae sollicitudin. Pellentesque habitant morbi tristique senectus et netus et malesuada fames ac turpis egestas. Donec eget blandit metus. Suspendisse vel orci fermentum, bibendum quam</p>
  </div>
  <div class="abs rule" style="left:617px;top:2189px"></div>
  <div class="abs step" style="left:617px;top:2232px">
    <h4>4. You will receive the money transferred</h4>
    <p>Lorem ipsum dolor sit amet, consectetur adipiscing elit. Donec lobortis nisi vel lectus mattis venenatis. Etiam iaculis volutpat congue. Nam eu faucibus massa. Praesent congue et neque vitae sollicitudin. Pellentesque habitant</p>
  </div>

  <section class="abs quote" role="img" aria-label="Blue-tinted photo of a scattered stamp and coin collection">
    <p class="serif-i">We have been in the stamp and coin trade<br>for nearly 100 years.</p>
  </section>

  <footer class="abs footer">
    <h5 style="left:172px">Kundenservice</h5>
    <ul style="left:172px"><li>Vertrauensgarantie</li><li>Versand</li></ul>
    <h5 style="left:385px">Kontakt</h5>
    <ul style="left:385px"><li>Kontakt</li><li>Impressum</li></ul>
    <h5 style="left:597px">Information</h5>
    <ul style="left:597px"><li>&nbsp;&nbsp; AGB</li><li>&nbsp;&nbsp; Widerruf</li><li>&nbsp;&nbsp; Datenschutz</li></ul>
    <div class="phone">Call 9831704400</div>
    <div class="mail">Email : info@briefhaus-tanner.ch</div>
    <div class="social"><i></i><span>Like Us<br>on Friendspace</span></div>
  </footer>

  <div class="abs legal">
    <p style="top:20px">Copyrights © 2020 All Rights Reserved</p>
    <p style="top:40px">Terms of Use / Privacy Policy</p>
  </div>

</div>
</body>
</html>
```